High end, luxury real estate property brochure

I need to have a property Brochure with 10-15 pages that will allow me to enter 30-40 photos and content about the home. It needs to be very high end and able to be edited in either word or publisher. I want to be able to use the pages individually when appropriate and then all together for larger homes. I need the template back by early Wednesday morning. Ideally, the brochure will be like a small booklet with a place for photos and content on the front and back of the pages. I need to add my company's logo and my photo to the project along with our office address etc..
Updates

Project Deadline Extended
Reason: I have decided to purchase more than one design and want to extend time for additional submissions.

Target Market(s)

Home Buyers in the Midwest (Indiana)

Industry/Entity Type

Real Estate Agent

Font styles to use
Serif

Requirements
Must have
• Graphically appealing. Integrated look between the pages. Several places for me to add photos of different sizes to highlight the homes features. The ability for me to change font, font colors, background colors, etc... Must have a high end, luxury feel. I will be adding descriptions and content about the photos so I need areas to add that information. I want the project to be able to be printed as a booklet for larger homes and to be able to use parts of the brochure for smaller homes as I won't have as many photos. Resolution must be fantastic. Clean lines.
Nice to have
• I am with Brandt Okafor Realty and our colors our logo is red so many of our publications are in Black and red. Dorian Pratt Promo Studios is a program that has some high end marketing pieces and designs that I like. I prefer the designs in the slate and black colors.
Should not have
• Cartoons graphics, pastel colors, "busy" designs.

```html
<!DOCTYPE html>
<html lang="en">
<head>
<meta charset="utf-8">
<title>Brandt Okafor Realty – Property Brochure</title>
<link href="https://fonts.googleapis.com/css2?family=Arvo:wght@400;700&family=Arimo:wght@400;700&family=Tinos:ital@0;1&display=swap" rel="stylesheet">
<style>
:root{
  --red:#c0121c;
  --red-deep:#7d0a10;
  --red-bright:#d81a24;
  --ink:#1e1e1e;
  --text:#333;
  --muted:#555;
  --paper:#ffffff;
  --paper-shade:#ececec;
  --backdrop:#a9a9a9;
  --panel-dark:#262626;
}
*{box-sizing:border-box;margin:0;padding:0}
html,body{width:857px;height:1200px;overflow:hidden}
body{background:var(--backdrop);position:relative;font-family:"Arimo",Arial,sans-serif;color:var(--text)}
.spread{position:absolute;left:46px;width:772px;height:499px;background:var(--paper)}
.spread--team{top:53px}
.spread--home{top:653px}
.abs{position:absolute}
.body-copy{font-size:6.3px;line-height:9.4px;color:var(--text)}
.body-copy p{margin-bottom:6px}
.heading{font-family:"Arvo",Georgia,serif;font-weight:700;color:var(--red)}
.subhead{font-family:"Arvo",Georgia,serif;font-weight:700;color:var(--red);font-size:7.2px;margin:2px 0 5px}
.pull-quote{font-family:"Tinos",Georgia,serif;font-style:italic;color:var(--red);font-size:7.4px;line-height:10.8px}
.quote-bar{position:absolute;width:4px;background:var(--red)}
.photo{position:absolute}
.photo--cut{clip-path:polygon(0 0,100% 0,100% 90%,91% 100%,0 100%)}
.photo--framed{outline:1px solid var(--red);outline-offset:0}
.member-name{font-size:6.6px;letter-spacing:.8px;color:var(--red);font-weight:700;text-transform:uppercase}
.member-role{font-size:6.6px;font-weight:700;color:var(--ink);margin:3px 0 3px}
.member-bio{font-size:6.1px;line-height:9px;color:var(--text)}
.page-tab{position:absolute;background:var(--red);color:#fff;font-size:7px;font-weight:700;display:flex;align-items:center;justify-content:center}
/* spread 1 */
.page--letter{position:absolute;left:0;top:0;width:386px;height:499px;background:linear-gradient(90deg,var(--red-deep),var(--red-bright) 70%,var(--red-deep))}
.page--letter .sheet{position:absolute;left:17px;top:17px;width:351px;height:466px;background:linear-gradient(90deg,#fff 60%,#ebebeb)}
.page--team{position:absolute;left:386px;top:0;width:386px;height:499px;background:linear-gradient(90deg,#e6e6e6,#fff 12%,#fff 80%,#f0f0f0)}
/* spread 2 */
.dark-panel{background:var(--panel-dark);color:#e6e6e6}
.dark-panel .body-copy{color:#ddd}
.dark-panel .subhead{color:#fff}
.red-panel{background:var(--red)}
.red-panel .body-copy{color:#fbd7d9}
.photo-caption{font-size:6.4px;font-weight:700;color:#fff;line-height:8.4px}
</style>
</head>
<body>

<section class="spread spread--team">
  <div class="page--letter">
    <div class="sheet"></div>
    <div class="photo photo--cut" role="img" aria-label="Portrait photo of the agent" style="left:26px;top:53px;width:114px;height:172px;background:linear-gradient(160deg,#c7cdd2,#8f8a86 55%,#3c4450)"></div>
    <div class="abs" style="left:26px;top:237px;width:122px">
      <div class="member-name">Ommolup Taturcip</div>
      <div class="member-role">Occatur Macores</div>
      <div class="member-bio">Apediaest od moluptur arcium sequiam, ut andaeperis dus remquos ad quibustia nonemquidus ad quianditae non repelestio. Me nonsed ma natet dunto tempore sapel.</div>
    </div>
    <div class="quote-bar" style="left:26px;top:361px;height:116px"></div>
    <p class="pull-quote abs" style="left:42px;top:359px;width:122px">Em et offici officata dolum debis rereiust eumquae sanihic tectius quiatae rionse porehen ecepero blamus aspeditin prorehent. Hent que maximust, officiatis eos earum fugiam, quia vernam quam, atur secte preprer feritio blaces pedic tescil es si rerspic te et quat et faciis dolutem.</p>

    <h1 class="heading abs" style="left:167px;top:51px;width:200px;font-size:15.5px;line-height:18px">Edmi aut venis diosti, eosaut dolorem recatur</h1>
    <div class="body-copy abs" style="left:167px;top:114px;width:192px">
      <p>Sequam, nia quia qui oditionectur ma dolupta estrum etur reperesequas rerereiciti ideri reptatio. Ipsandanias consenimus moditio odis aliam lam qui accum quo con con raes essed quam, nus ius dollati orrum, iur sapidundist fugit aliquasi senist, voloriaet lis quam aceat.</p>
      <p>Itae volupie nderum lanti ut voles cusdae perum dolorib usamus que occus autatiusa volum suntiae dolupta estrupictur sinvendesedi beris sit apel inihilis dolupta tibusdae serfers perrupt aturiandant aut dolupid ebitiis estrunt, cus rem eveniatem as rem ratur re perovitat.</p>
      <div class="subhead">At que cus ma quidendem psaperum soluptat</div>
      <p>Pis aut eumetusae volenih icillore consed mil isi necepud andaero cor sunt iundani magnatur acerferia quiat ut evere, conse si sit occatur ma cores perum qui cusam ariorum antiasit quo consed etus sit quatem fugia im harum eiciist es sequi alit, el eicte vellest ionsequ asitate maionsequi dolorrum sunt equibus, sunt aut ut ut as ut excerum rest expedit ipsunt, omni quam, tet pro esed et ommos nullece rehenis cipsapid magnatusct et am eatet ommolup tatur?</p>
      <p>Nem reptate nderfer feriatiorrum quassitae. Ota con cum quam secepernam et lab inum vellacestis quasper eressitenit, odi restinimus, ut et aut autemperrum unt ut explaut quos vendigni deliciendi dolori dis a id quibus etus, sae quo es acimagnat.</p>
      <p>Is dolla et mo blam dolorende latem. Itate labor aut quam aut il moluptat aute qui blabo. Itam quam que que net volorep ernat. Nam lande vid ullupta vel ipsae liatemporro volorep eruptatus el id qui.</p>
    </div>
    <div class="abs" role="img" aria-label="Agent signature" style="left:167px;top:420px;width:70px;height:28px;background:linear-gradient(90deg,#f1f1f1,#e4e4e4)"></div>
    <div class="abs" style="left:167px;top:461px;font-size:6.6px;line-height:9px;color:var(--ink)"><b>OMMOLUP TATURCIP</b><br>OCCATUR MACORES</div>
  </div>

  <div class="page--team">
    <div class="page-tab" style="left:261px;top:0;width:97px;height:35px;font-family:'Arvo',serif;font-size:7px">Otae veriame omnim</div>
    <div class="page-tab" style="left:358px;top:0;width:28px;height:35px;background:var(--ink)">1</div>
    <h2 class="heading abs" style="left:28px;top:51px;font-size:15.5px;line-height:19px">THE BOR<br>TEAM</h2>
    <div class="quote-bar" style="left:28px;top:99px;height:136px"></div>
    <p class="pull-quote abs" style="left:42px;top:97px;width:108px">corepta cone dolo elendaepe verum voluptate lam et que Excepell utempostis nitatusandus sed moluptatur? Quiae landis atem quodignati ut aribus dolor rentis aut pliqui utatur? Qui sit, quias et vendipiet parchita debitissunt que voluptatur, nessi dolecto offic te conra</p>

    <div class="photo photo--cut photo--framed" role="img" aria-label="Team member portrait" style="left:144px;top:53px;width:98px;height:124px;background:linear-gradient(160deg,#d9d5cf,#a98a6c 55%,#3a3632)"></div>
    <div class="photo photo--cut photo--framed" role="img" aria-label="Team member portrait" style="left:261px;top:53px;width:98px;height:124px;background:linear-gradient(160deg,#b8262a,#c49b82 50%,#1f2228)"></div>
    <div class="abs" style="left:144px;top:185px;width:100px">
      <div class="member-name">Elendaepe Verum</div>
      <div class="member-role">Voluptate Lametue</div>
      <div class="member-bio">Ucia cullabo. Itatio. Itas asimusam nonsenducias nobitem ut quis siminte incto quas doloribus. Namus delentota reiciis doloria turibuscium.</div>
    </div>
    <div class="abs" style="left:261px;top:185px;width:100px">
      <div class="member-name">Magnimp Orendanie</div>
      <div class="member-role">Doluptati Cullenty</div>
      <div class="member-bio">Occus, offici beaqui odit magnis et oditio. Sequas nissin ratatur aut fugiae nonseces conseni, cum que doluptati cullente exerion senissimenis lamusae.</div>
    </div>

    <div class="photo photo--cut photo--framed" role="img" aria-label="Team member portrait" style="left:28px;top:263px;width:98px;height:124px;background:linear-gradient(160deg,#6f6a62,#a0816a 50%,#2a2624)"></div>
    <div class="photo photo--cut photo--framed" role="img" aria-label="Team member portrait" style="left:144px;top:263px;width:98px;height:124px;background:linear-gradient(160deg,#8c7a62,#c79a78 50%,#5a3a26)"></div>
    <div class="photo photo--cut photo--framed" role="img" aria-label="Team member portrait" style="left:261px;top:263px;width:98px;height:124px;background:linear-gradient(160deg,#f2f2f2,#d3a98d 55%,#2c2c30)"></div>
    <div class="abs" style="left:28px;top:398px;width:100px">
      <div class="member-name">Voluptat Estondae</div>
      <div class="member-role">Essitas Nobitatenis</div>
      <div class="member-bio">Lor sunto quamet accum ex et eatis es adit esto voluptat pro estorehendae et illab ipitis essitas nobitatenis. Namus delentota venim reiciis doloria turibuscium exceroped corepta cone</div>
    </div>
    <div class="abs" style="left:144px;top:398px;width:100px">
      <div class="member-name">Velen Dipsant</div>
      <div class="member-role">Quae Eatempore</div>
      <div class="member-bio">Pelesequis et quasperrat pernat inctius prerum, ad quia vollaccae pos dero blacepe sequae vel eat enducilit, nimo omni dolupta sperciis eosa moloris es.</div>
    </div>
    <div class="abs" style="left:261px;top:398px;width:100px">
      <div class="member-name">Beate Volupier</div>
      <div class="member-role">Volupienis Maximint</div>
      <div class="member-bio">Liaeptur asit aspe nimo to volorio corpos endae nobissit ent exped exceseque provit earum facea quibeaqui aliquatur, rectur, comni rentio. Ex emaximint vent, sus quatiat</div>
    </div>
  </div>
</section>

<section class="spread spread--home">
  <div class="photo" role="img" aria-label="Photo of a timber home in front of snowy mountains" style="left:0;top:0;width:386px;height:229px;background:linear-gradient(180deg,#a9c4dc 0%,#d6dfe6 28%,#6f8090 42%,#5e7a48 62%,#8a5a3c 75%,#c9b87a 100%)"></div>
  <div class="page-tab" style="left:0;top:0;width:26px;height:35px">2</div>

  <div class="dark-panel abs" style="left:206px;top:112px;width:154px;height:368px;padding:26px 13px 0 13px">
    <div class="body-copy">
      <p>Nienihicium idem facepe peruptatque ipitem fugitatas ari abor aut qui te que simi, to optaquia el moluptur?</p>
      <p>Abo. Itam quaspeditium aut hariatur se eos sinctae necte quatem none consequam voluptat int que delitat qui officaecta pos es sunt, sequae volendiaest, sequod qui occaborae. Dolor sinctatem. Bus, asped maxime expercist ut expe nihicillam hillandam repellores quiam, nienis vent ex eos sunt asperior res etur sint.</p>
      <p>Dusdae nimodicae endemqui conet lique od et dolore verfere stioreh eniaectation ratenem cor acitate volorem ad quis mod utatum solore il is et ped mincitem verfernate pores qui aut quae rem reicitam quatur, sit voloreiur, cum quistorempos rempos que doluptasi re, omnitas dolution cus ent eicia in ni doluptas eum latiant.</p>
      <div class="subhead">magnihi ligentiate voluptiae</div>
      <p>Ibust, consequid berunde lessit quiae rempor ad ut acimagnates vit planden iendantia cum iunt que seque necum hit quia voluptat ped quidipi ctotaesto cum qui vercius aceseca erisquo blabo. Sed molupta tescil maxim quat volest laces nemporecaero dolora idest ilia dolupti untecae vel maximin imaximus endent es dit dit, sequunt verchiti dempore et faccabore, nonserio. Et ut opta vero qui aturemporae. Et vel eum quatem venist, aciunde ritatatur?</p>
    </div>
  </div>

  <h2 class="heading abs" style="left:26px;top:245px;font-size:11.6px">Ducia susd isatruh arunts</h2>
  <div class="quote-bar" style="left:26px;top:269px;height:50px"></div>
  <p class="pull-quote abs" style="left:40px;top:267px;width:140px">Arut esciae coril, temporeri dolorio simus. Ficte nonse ist, vel id qui conse arunt quam aligeni aboritatem velessitia volupta velles dolenih illaute mporeiundent hit.</p>
  <div class="body-copy abs" style="left:26px;top:347px;width:156px">
    <p>Ihitiae. Eperitaturio consequis dolorro consequi abore aut licaessitiis ipsamus corepudis aperro debit eturemo te dolut aut quis is site nem asinctur remporio doluptatibus verum qui ut hit inis que venimos dellibusdae que comnis mod quia volori audandiat dit aut fugitio blate precae es prectotat laborum ipsuntur?</p>
    <p>Otate sit, unt. Molora idunt que dolutat entotatis aspeliaepere di con esequod itiuntianda ania que et.</p>
    <p>Accullab ilitatam, occupiendae rerferovid que pedionse volo con conseque reptatur acerumquos est occum etur, si int.</p>
  </div>

  <div class="red-panel abs" style="left:386px;top:0;width:206px;height:229px;padding:53px 26px 0 26px">
    <div class="heading" style="color:#fff;font-size:7.4px;line-height:9.6px;margin-bottom:14px">Nem que mintem eum liquibu sanditas assunt eos etur?</div>
    <div class="body-copy">
      <p>Nient, sum etur autatest fugiae natem. Nam fugit eum atatem elesto tectem fugia similiq uunduci molore ommolor re, consers perferia voloremped eate nus, susande nducid qui nobitatint quaspelibus, sequatqui omnim faccaerum rerovitassi sitiur?</p>
      <p>Quia namusdam nos aligenditat auditam, to inctur? Nam reprae exera quam aperior rem corepudam consequatem acidi corerum idusam as dolor sum aceptas audis eostio beatur?</p>
      <p>At doluptata doluptae corrum volupta turibusdae ommolor uptate nihillias vit occabo. Nam fugit eruptisquam, oditis esti nobitat ibusae.</p>
    </div>
  </div>
  <div class="photo" role="img" aria-label="Photo of a stone-clad home entrance with porch" style="left:592px;top:0;width:180px;height:229px;background:linear-gradient(165deg,#e7e2d6 0%,#b9a88c 40%,#8b7a62 65%,#4f5f38 85%,#6b8a3c 100%)"></div>
  <div class="page-tab" style="left:746px;top:0;width:26px;height:35px">3</div>
  <div class="photo-caption abs" style="left:699px;top:208px">QUIS RERIOS<br>SIME CUSAT</div>

  <div class="quote-bar" style="left:414px;top:239px;height:28px"></div>
  <p class="pull-quote abs" style="left:429px;top:237px;width:330px">Ut laborio riaspe eosam qui asimi, quamenderum qui con con nihilia vel eos iuntorporro in nulpa volestiist, occum ullatium escideliqui dio. Name vent et poreius, quistrum aditatem aut vel maximusam adionec aborrum, illa velliqu atempor uptatiis at qui utet aped maioribeaque.</p>

  <div class="photo" role="img" aria-label="Photo of a bright living room with white sofas and tall windows" style="left:386px;top:283px;width:180px;height:216px;background:linear-gradient(180deg,#6d5a42 0%,#b8a584 30%,#d9d3c4 60%,#efebe2 100%)"></div>
  <div class="body-copy abs" style="left:592px;top:283px;width:156px">
    <p>Luptamus et acepere veliquos ex et lab id et ea sum quiate vero volorem id quam, omniminullam id ea delitiur as re a dit landell acernam quis exerunt</p>
    <p>Bearum unt. Acculpa iunt, in corrum dolupti cus magnis esequid usaperuptaes porem ideliquiam quasitatemo test odite qui reriorro idi ut et idia del et et volo tem nonsed quia doluptate provitaqui aut entures venimaxime parunt.</p>
    <div class="subhead">Quame quatum excea conseque</div>
    <p>Esequibus ea aut voluptatium ra pos dolorem nimus nonsequ asincte mperchi cidenditem intur, quossi quis autes et offic to beat il ese ventior poribus magnitae aut eture venihit, sim iusdae nullorporae litiis dipsandunt repudia volorio nsernam, con porernquatia qui tet et latectati dolupta nossit ommodis eate si ipsamquam fugit explibuscim es everrum fugit ma quia ditat fugitae. Niatiae pa quis dis quos acient aperferio odionseres quost.</p>
  </div>
</section>

</body>
</html>
```